Product label and brand logo for Superfood powder

We need a product label (incl. logo) for a new plant-based Superfood powder called "MyLunaBrisa Health & Wellness Protein" ("MyLunaBrisa" being the brand). The powder formula is comprised of various Superfoods that each offer a unique benefit to the customer. On top of that the formular includes real coffee for excellent taste. This is a premium product and some ingredients even come from organic sources. I've included an extended briefing with examples as a PDF. The final design should communicate wellbeing, health, wellness rather than target the sport and fitness crowd (as most protein powders do).
Target Market(s)
Health & Wellness Space
Industry/Entity Type
Health And Wellness
Requirements
Must have
- Please see attached PDF.
Nice to have

```html
<!DOCTYPE html>
<html lang="de">
<head>
<meta charset="utf-8">
<title>MyLunaBrisa Health &amp; Wellness Protein – Etikett</title>
<link rel="stylesheet" href="https://fonts.googleapis.com/css2?family=Oswald:wght@500;700&family=Roboto:wght@300;400;700&display=swap">
<style>
  :root{
    --bg-light:#d9d9d9;
    --bg-dark:#8c8c8c;
    --brown-deep:#2a120c;
    --brown:#3e1d16;
    --brown-mid:#5a2a1e;
    --green:#6f9b3d;
    --ink:#231f20;
    --white:#ffffff;
    --orange-light:#ffd07a;
    --orange:#f7921e;
    --silver:#9a9a9a;
  }
  *{box-sizing:border-box;margin:0;padding:0}
  html,body{width:1200px;height:1200px;overflow:hidden}
  body{
    background:linear-gradient(135deg,var(--bg-dark) 0%,var(--bg-light) 35%,var(--bg-dark) 100%);
    font-family:"Roboto",Arial,sans-serif;
    position:relative;
  }

  /* Brand mark */
  .brand-mark{
    position:absolute;left:78px;top:120px;
    display:flex;align-items:center;gap:18px;
  }
  .brand-mark__dot{width:46px;height:46px;border-radius:50%;background:var(--green)}
  .brand-mark__name{
    font-family:"Roboto",Arial,sans-serif;font-weight:300;
    font-size:58px;color:var(--brown-deep);letter-spacing:1px;
  }

  /* Label component */
  .label{
    position:absolute;display:flex;flex-direction:column;
    background:var(--white);overflow:hidden;
  }
  .label--pouch{left:44px;top:560px;width:544px;height:478px;font-size:16px}
  .label--jar{left:632px;top:464px;width:488px;height:608px;font-size:18px}

  .label__band{
    height:.9em;flex:none;
    background:linear-gradient(90deg,var(--brown-deep),var(--brown-mid) 50%,var(--brown-deep));
  }
  .label__body{
    flex:1;display:flex;flex-direction:column;align-items:center;justify-content:flex-start;
    padding-top:1.6em;
  }
  .label__brand{display:flex;align-items:center;gap:.45em}
  .label__brand-dot{width:1em;height:1em;border-radius:50%;background:var(--green)}
  .label__brand-name{font-weight:300;font-size:1.9em;color:var(--brown-deep)}

  .label__claim{
    margin-top:.9em;font-family:"Oswald",sans-serif;font-weight:500;
    font-size:2.15em;line-height:1;color:var(--green);letter-spacing:.01em;
    transform:scaleY(1.08);
  }
  .label__title{
    display:flex;align-items:center;gap:.35em;
    font-family:"Oswald",sans-serif;font-weight:700;font-size:2.7em;line-height:1.05;
    color:var(--ink);letter-spacing:.02em;
  }
  .label__title-o{
    width:.92em;height:.92em;border-radius:50%;
    border:.07em solid var(--ink);
    background:radial-gradient(circle,#a0602e 0%,#6b3a1b 60%,#3b1d0d 100%);
  }
  .label__flavour{margin-top:.75em;font-size:1.15em;color:var(--ink);letter-spacing:.03em}

  .label__base{
    position:relative;flex:none;height:10em;
    background:linear-gradient(180deg,var(--brown) 0%,var(--brown-deep) 100%);
  }
  .label__stats{
    position:absolute;left:50%;top:-2.6em;transform:translateX(-50%);
    display:flex;gap:3.6em;
  }
  .stat{
    width:5.1em;height:5.1em;border-radius:50%;
    background:var(--ink);border:.3em solid var(--white);
    box-shadow:0 0 0 .25em var(--ink);
    display:flex;flex-direction:column;align-items:center;justify-content:center;
    color:var(--white);font-size:1em;line-height:1.05;text-align:center;
  }
  .stat__value{font-size:1.1em}
  .stat__unit{font-size:1.1em}

  .label__promo{
    position:absolute;left:50%;top:3.6em;transform:translateX(-50%);
    width:25em;height:5.6em;
  }
  .promo__cup{
    position:absolute;left:0;top:0;width:6.2em;height:5.4em;border-radius:0 0 2.2em 2.2em;
    background:radial-gradient(ellipse at 50% 25%,#d9a05c 0%,#6b3a1b 45%,#2b1408 100%);
  }
  .promo__ribbon{position:absolute;left:5.2em;top:.2em;width:19.8em;height:4.6em}
  .promo__text{
    position:absolute;left:8.4em;top:.65em;width:14em;color:var(--ink);text-align:left;
  }
  .promo__headline{font-size:1.05em;letter-spacing:.02em}
  .promo__extras{font-size:.62em;font-weight:700;margin-top:.25em;word-spacing:.2em}
  .promo__free{font-size:.8em;color:var(--white);margin-top:.2em;padding-left:2em;word-spacing:.4em}
  .label__net{
    position:absolute;left:50%;bottom:.5em;transform:translateX(-10%);
    color:var(--white);font-size:.62em;white-space:nowrap;
  }
</style>
</head>
<body>

  <div class="brand-mark">
    <span class="brand-mark__name">MyLunaBrisa</span>
    <span class="brand-mark__dot"></span>
  </div>

  <section class="label label--pouch">
    <div class="label__band"></div>
    <div class="label__body">
      <div class="label__brand"><span class="label__brand-name">MyLunaBrisa</span><span class="label__brand-dot"></span></div>
      <div class="label__claim">HEALTH &amp; WELLNESS</div>
      <div class="label__title"><span>P</span><span>R</span><span class="label__title-o" role="img" aria-label="Kaffeebohnen im Buchstaben O"></span><span>T</span><span>E</span><span>I</span><span>N</span></div>
      <div class="label__flavour">Kaffeegeschmack</div>
    </div>
    <div class="label__base">
      <div class="label__stats">
        <div class="stat"><span class="stat__value">20 g</span><span class="stat__unit">Protein</span></div>
        <div class="stat"><span class="stat__value">4 g</span><span class="stat__unit">BCAA</span></div>
        <div class="stat"><span class="stat__value">4 g</span><span class="stat__unit">Glutamin</span></div>
      </div>
      <div class="label__promo">
        <svg class="promo__ribbon" viewBox="0 0 396 92" preserveAspectRatio="none" aria-hidden="true">
          <defs><linearGradient id="ribbon-a" x1="0" x2="1"><stop offset="0" stop-color="#ffe3a8"/><stop offset="1" stop-color="#f7921e"/></linearGradient></defs>
          <polygon points="0,2 394,2 346,46 394,90 0,90" fill="url(#ribbon-a)" stroke="#a3a3a3" stroke-width="4"/>
        </svg>
        <div class="promo__cup" role="img" aria-label="Tasse Kaffee mit Kaffeebohnen"></div>
        <div class="promo__text">
          <div class="promo__headline">MIT ECHTEM KAFFEE</div>
          <div class="promo__extras">+ VITAMINE &nbsp; + MINERALSTOFFE</div>
          <div class="promo__free">Laktosefrei Glutenfree</div>
        </div>
      </div>
      <div class="label__net">e 1.000 g / 25 Portionen</div>
    </div>
  </section>

  <section class="label label--jar">
    <div class="label__band"></div>
    <div class="label__body">
      <div class="label__brand"><span class="label__brand-name">MyLunaBrisa</span><span class="label__brand-dot"></span></div>
      <div class="label__claim">HEALTH &amp; WELLNESS</div>
      <div class="label__title"><span>P</span><span>R</span><span class="label__title-o" role="img" aria-label="Kaffeebohnen im Buchstaben O"></span><span>T</span><span>E</span><span>I</span><span>N</span></div>
      <div class="label__flavour">Kaffeegeschmack</div>
    </div>
    <div class="label__base">
      <div class="label__stats">
        <div class="stat"><span class="stat__value">20 g</span><span class="stat__unit">Protein</span></div>
        <div class="stat"><span class="stat__value">4 g</span><span class="stat__unit">BCAA</span></div>
        <div class="stat"><span class="stat__value">4 g</span><span class="stat__unit">Glutamin</span></div>
      </div>
      <div class="label__promo">
        <svg class="promo__ribbon" viewBox="0 0 396 92" preserveAspectRatio="none" aria-hidden="true">
          <defs><linearGradient id="ribbon-b" x1="0" x2="1"><stop offset="0" stop-color="#ffe3a8"/><stop offset="1" stop-color="#f7921e"/></linearGradient></defs>
          <polygon points="0,2 394,2 346,46 394,90 0,90" fill="url(#ribbon-b)" stroke="#a3a3a3" stroke-width="4"/>
        </svg>
        <div class="promo__cup" role="img" aria-label="Tasse Kaffee mit Kaffeebohnen"></div>
        <div class="promo__text">
          <div class="promo__headline">MIT ECHTEM KAFFEE</div>
          <div class="promo__extras">+ VITAMINE &nbsp; + MINERALSTOFFE</div>
          <div class="promo__free">Laktosefrei Glutenfree</div>
        </div>
      </div>
      <div class="label__net">e 1.000 g / 25 Portionen</div>
    </div>
  </section>

</body>
</html>
```